Online only (mobile devices) 50th Birthday Invitation

Design an online (surprise) 50th Birthday dinner invitation for a female (Dellaphine). It should be elegant and similar to the examples uploaded. Will provide restaurant address details, times and RSVP details to winning designer. Please mock up.
Details should be:
Saturday 12th April 2025
Arrive between 6:30pm and 6:45pm
Restaurant Name
Restaurant Address
RSVP name and mobile phone by Friday 4 April 2025
Target Market(s)
The person's friends and family
Requirements
Must have
- Elegance and class
Nice to have
- Gold or silver colouring

```html
<!DOCTYPE html>
<html lang="en">
<head>
<meta charset="UTF-8">
<title>Dellaphine – 50th Birthday Invitation</title>
<link rel="stylesheet" href="https://fonts.googleapis.com/css2?family=Cinzel:wght@400;700&family=Cormorant+Garamond:wght@600&family=Great+Vibes&display=swap">
<style>
  :root {
    --ink: #050505;
    --gold-light: #f6e27a;
    --gold: #d4a935;
    --gold-deep: #8a6a1c;
    --white: #ffffff;
  }
  * { box-sizing: border-box; margin: 0; padding: 0; }
  html, body { width: 841px; height: 1200px; overflow: hidden; background: var(--ink); }
  .invitation {
    position: relative; width: 841px; height: 1200px;
    background: var(--ink); overflow: hidden; color: var(--white);
  }
  .sparkle-field {
    position: absolute; inset: 0;
    background:
      radial-gradient(circle at 190px 210px, rgba(255,255,255,0.03) 0 45px, transparent 47px),
      radial-gradient(circle at 420px 90px, rgba(255,255,255,0.025) 0 70px, transparent 72px),
      radial-gradient(circle at 700px 300px, rgba(255,255,255,0.02) 0 35px, transparent 37px),
      radial-gradient(ellipse at 65% 110%, rgba(92,70,20,0.8) 0%, rgba(60,45,12,0.5) 30%, transparent 60%),
      linear-gradient(to bottom, transparent 55%, rgba(70,54,16,0.4) 85%, rgba(92,70,20,0.55) 100%);
  }
  .artwork { position: absolute; inset: 0; width: 841px; height: 1200px; }
  .col { position: absolute; left: 371px; width: 400px; text-align: center; }
  .script { font-family: "Great Vibes", cursive; font-weight: 400; }
  .caps { font-family: "Cinzel", serif; font-weight: 400; line-height: 1.3; }
  .age-suffix { position: absolute; left: 728px; top: 78px; font-size: 36px; }
  .occasion { top: 388px; font-size: 46px; line-height: 1.1; }
  .lead-in { top: 445px; font-size: 14px; line-height: 1.5; }
  .guest-name { top: 490px; font-size: 66px; line-height: 1.2; }
  .date { top: 633px; font-size: 24px; }
  .arrival { top: 669px; font-size: 18px; }
  .venue { top: 765px; font-size: 24px; line-height: 1.35; }
  .rsvp { top: 962px; font-size: 21px; line-height: 1.45; }
</style>
</head>
<body>
<main class="invitation">
  <div class="sparkle-field" role="img" aria-label="Soft bokeh lights and fine gold glitter dust rising from the bottom"></div>

  <svg class="artwork" viewBox="0 0 841 1200" aria-label="Happy Birthday 50">
    <defs>
      <linearGradient id="goldFoil" x1="0" y1="0" x2="1" y2="1">
        <stop offset="0" stop-color="#f6e27a"/>
        <stop offset="0.45" stop-color="#d4a935"/>
        <stop offset="0.8" stop-color="#8a6a1c"/>
        <stop offset="1" stop-color="#e8c75a"/>
      </linearGradient>
    </defs>
    <text class="greeting-band" transform="translate(128 1188) rotate(-90)" font-family="Cinzel, serif" font-weight="700"
          font-size="122" fill="url(#goldFoil)" textLength="1175" lengthAdjust="spacingAndGlyphs">HAPPY BIRTHDAY</text>
    <text class="age" x="388" y="405" font-family="'Cormorant Garamond', serif" font-weight="600"
          font-size="500" style="font-variant-numeric: lining-nums; font-feature-settings: 'lnum' 1;"
          fill="url(#goldFoil)" textLength="366" lengthAdjust="spacingAndGlyphs">50</text>
  </svg>

  <div class="age-suffix script">th</div>
  <p class="col occasion script">Birthday</p>
  <p class="col lead-in caps">JOIN US TO<br>CELEBRATE 50TH BIRTHDAY OF</p>
  <h1 class="col guest-name script">Dellaphine</h1>
  <p class="col date caps">Saturday 12th April 2025</p>
  <p class="col arrival caps">between 6:30pm &amp; 6:45pm</p>
  <p class="col venue caps">Restaurant Name<br>Restaurant Address</p>
  <p class="col rsvp caps">RSVP name and mobile phone<br>by Friday 4 April 2025</p>
</main>
</body>
</html>
```